Brantwell Group needs a business card design

We need a new business card design using the logo recently selected in a logo competition on Pixel Forum. Our business is a consultancy specializing in aviation and energy and the winning business card design will promote an image of precision and professionalism with creativity.

Please use the logo with the name on the front of the card and use a complementary font. Make the back white with either the light grey or dark grey logo.

Target Market(s)

Senior finance and legal leaders at aviation and energy companies

Industry/Entity Type

Management Consulting

Contact Information for Business Card

Peter Haldane
President
Brantwell Group

www.brantwellgroup.example

(555) 304-6198
ph@brantwellgroup.example

Requirements
Must have
• Professional font that goes well with the logo font

```html
<!DOCTYPE html>
<html lang="en">
<head>
<meta charset="utf-8">
<title>Brantwell Group – Business Card</title>
<link rel="stylesheet" href="https://fonts.googleapis.com/css2?family=Lato:ital,wght@0,400;0,700;1,400&display=swap">
<style>
  :root {
    --page-bg: #e8e6e2;
    --card-bg: #ffffff;
    --navy: #1d3f73;
    --ink-grey: #5a5a5a;
    --mark-grey: #666666;
    --rule-grey: #b8b8b8;
    --shadow: rgba(0, 0, 0, 0.18);
  }
  * { box-sizing: border-box; margin: 0; padding: 0; }
  html, body {
    width: 1200px;
    height: 900px;
    overflow: hidden;
  }
  body {
    background: var(--page-bg);
    font-family: "Lato", "Helvetica Neue", Arial, sans-serif;
    display: flex;
    flex-direction: column;
    align-items: center;
    justify-content: center;
    gap: 40px;
  }
  .card {
    width: 630px;
    height: 360px;
    background: var(--card-bg);
    box-shadow: 0 6px 18px var(--shadow);
    position: relative;
  }

  /* Back */
  .card-back {
    display: flex;
    align-items: center;
    justify-content: center;
  }
  .back-name {
    color: var(--mark-grey);
    font-weight: 400;
    font-size: 46px;
    letter-spacing: 0.12em;
    text-transform: uppercase;
  }

  /* Front */
  .card-front {
    display: flex;
    align-items: center;
    padding: 0 40px 0 44px;
  }
  .brand {
    width: 250px;
    text-align: center;
    color: var(--navy);
    font-weight: 400;
    text-transform: uppercase;
  }
  .brand-line-main {
    display: block;
    font-size: 32px;
    letter-spacing: 0.06em;
    line-height: 1.1;
  }
  .brand-line-sub {
    display: block;
    font-size: 17px;
    letter-spacing: 0.9em;
    margin-top: 10px;
    padding-left: 0.9em;
  }
  .divider {
    width: 1px;
    height: 150px;
    background: var(--rule-grey);
    margin: 0 34px 0 30px;
  }
  .contact {
    color: var(--ink-grey);
  }
  .person-name {
    color: var(--navy);
    font-weight: 700;
    font-size: 21px;
    line-height: 1.1;
  }
  .person-title {
    font-style: italic;
    font-size: 15px;
    margin-bottom: 16px;
  }
  .contact-list { list-style: none; }
  .contact-item {
    display: flex;
    align-items: center;
    gap: 9px;
    font-size: 16px;
    line-height: 1.55;
  }
  .contact-icon {
    width: 15px;
    height: 15px;
    fill: var(--navy);
    flex: none;
  }
</style>
</head>
<body>

  <section class="card card-back" aria-label="Card back">
    <span class="back-name">Brantwell Group</span>
  </section>

  <section class="card card-front" aria-label="Card front">
    <div class="brand">
      <span class="brand-line-main">Brantwell</span>
      <span class="brand-line-sub">Group</span>
    </div>

    <div class="divider"></div>

    <div class="contact">
      <p class="person-name">Peter Haldane</p>
      <p class="person-title">President</p>
      <ul class="contact-list">
        <li class="contact-item">
          <svg class="contact-icon" viewBox="0 0 16 16" aria-hidden="true">
            <path d="M3.5 1.5l2.5 0 1.2 3-1.6 1.1c.8 1.7 2.1 3 3.8 3.8l1.1-1.6 3 1.2v2.5c0 .8-.7 1.5-1.5 1.5C6.6 13 3 9.4 2 3 2 2.2 2.7 1.5 3.5 1.5z"/>
          </svg>
          <span>(555) 304-6198</span>
        </li>
        <li class="contact-item">
          <svg class="contact-icon" viewBox="0 0 16 16" aria-hidden="true">
            <path d="M1 3h14v10H1z M2 4l6 5 6-5" fill="var(--navy)"/>
            <path d="M2 4.2l6 4.8 6-4.8" fill="none" stroke="#fff" stroke-width="1.2"/>
          </svg>
          <span>ph@brantwellgroup.example</span>
        </li>
        <li class="contact-item">
          <svg class="contact-icon" viewBox="0 0 16 16" aria-hidden="true">
            <circle cx="8" cy="8" r="7"/>
            <g fill="none" stroke="#fff" stroke-width="1">
              <ellipse cx="8" cy="8" rx="3" ry="7"/>
              <path d="M1 8h14M2.2 4.5h11.6M2.2 11.5h11.6M8 1v14"/>
            </g>
          </svg>
          <span>www.brantwellgroup.example</span>
        </li>
      </ul>
    </div>
  </section>

</body>
</html>
```